Exciting Poster Project: 4 posters for Employee Benefit Program

We are an entrepreneurial healthcare IT company that is creating an internal campaign to launch our 2017 Culture and Professional Development goals for our internal staff.

We need 4 posters utilizing the 4 campaign logos (attached) that are tied together visually into a cohesive campaign.

A PPT is included that shows the other wall art that currently exists on the walls. The new posters will share a space with these pieces.

The posters may be mounted side by side, or stand alone on a wall- so the design should work both ways. Each poster should include its own icon and the tag line provided along with topics provided that fall under this category. The posters size can be dictated by your design, but the text should be legible from a minimum of 8 feet away.

At the bottom of each poster should include all 4 icons in order to tie the entire campaign together (perhaps they can be arranged together like a diamond shape with the primary one as the biggest diamond)

Our company website for our external branding is: www.pelmaroq.com
We have included our branding guidelines for our external brand, and ppts and graphics for our internal brand.

1) Poster 1:
a. Header: Better Today Than Yesterday
b. Sub-title: Personal and Professional Growth
c. Description: We are committed to helping you build on your strengths and passions and support you your career advancement goals. We have a variety of training and development programs available to help you reach your top potential!
Leadership Development Programs
1. Supervisor Training
2. Women’s Leadership
3. Leadership Meet-Ups
4. MBA Program
Staff Development
1. Continuing Education Fund
2. Book Club
3. Pelmaroq University
4. Mentorship
5. Learning Libraries
6. Department Wide Training Events

2) Poster 2:
a. Header: Perform at Highest Capacity
b. Sub-title: Be Your Best Self
c. Description: We are committed to providing programs that bring focus to your health and overall personal wellness to encourage a well balanced life
i. Healthy Living
1. Health and wellness seminars
2. Nutrition: Fruit Delivery
ii. Fitness:
1. Step Challenge
2. Virtual 5k
3. Recess
4. Golf Lessons
5. Ping Pong Club
iii. Creativity:
1. Painting
2. Photography Club
3. Virtual Trivia
iv. Mental Health:
1. Massage Therapy
2. EAP Education
v. Financial
1. 401(k)
2. Retirement education/financial planning seminars
3. Global Insurance Program education

3) Poster 3:
a. Header: Passionate Urgent and Driven to Success
b. Sub-Header: Innovation and Strategy
c. Description: We are committed to helping you connect the dots both in the industry and with our internal goals , mission, and vision.
i. Quarterly All-Hands
ii. Lumiverse
1. Internally: Departmental and Product Updates
2. Externally: Industry Knowledge
3. Culturally: Peer to Peer Community

4) Poster 4:
a. Header: Succeed as a Team
b. Sub-Header: Cultivating Collaboration
c. Description: We are committed to creating a culture of appreciation, teamwork, and supporting an open communication. All feedback and ideas are welcome here!
i. Team Building Events
1. Employee Focused
a. Summer Picnic
b. Employee Appreciation
c. Diwali
d. Holiday Party
e. Department Appreciation
2. Family Friendly
a. Halloween
b. Bring your Kids to Work Day
3. Awards
a. Peer to Peer: QuickNod Awards
b. Leadership: Crest of Merit
4. Surveys
a. New Hire
b. Employee Engagement
Updates

Target Market(s)

Internal Employees

Industry/Entity Type

Healthcare

Font styles to use
Sans Serif

Requirements
Must have
• Job Type: Posters
• Task Outline: Create Vector Art for 4 icons and 4 posters
• Fonts and Styles to Use: SourceSansPro
Nice to have
• There is an attachment with suggested concepts and styles that we like.
Should not have
• The poster should not be very wordy or hard to read in passing.

```html
<!DOCTYPE html>
<html lang="en">
<head>
<meta charset="utf-8">
<title>Perform at Highest Capacity</title>
<link rel="stylesheet" href="https://fonts.googleapis.com/css2?family=Source+Sans+3:wght@400;600;700;900&display=swap">
<style>
  :root {
    --blue: #2f56a8;
    --red: #a51c30;
    --purple: #6c2c8c;
    --slate: #939ea4;
    --gold: #fbb92f;
    --amber: #f8a030;
    --orange: #f47a25;
    --tangerine: #f5841f;
    --flame: #ef5b22;
    --ink: #1e1a16;
    --white: #ffffff;
  }
  * { margin: 0; padding: 0; box-sizing: border-box; }
  html, body { width: 927px; height: 1200px; overflow: hidden; }
  body { font-family: "Source Sans 3", "Source Sans Pro", sans-serif; }
  .poster { position: relative; width: 927px; height: 1200px; overflow: hidden; background: var(--gold); }

  .hero {
    position: absolute; left: 0; top: 0; width: 927px; height: 428px;
    background: radial-gradient(ellipse at 40% 45%, #ffffff 0%, #efedea 45%, #cfc8bf 100%);
    overflow: hidden;
  }
  .headline { position: absolute; font-weight: 900; letter-spacing: -4px; line-height: 1; }
  .headline.perform { left: 26px; top: 22px; font-size: 104px; color: var(--blue); }
  .headline.at { left: 400px; top: 62px; font-size: 68px; color: var(--blue); letter-spacing: -2px; }
  .headline.highest { left: 22px; top: 112px; font-size: 148px; color: var(--red); letter-spacing: -6px; }
  .headline.capacity { left: 54px; top: 240px; font-size: 140px; color: var(--blue); letter-spacing: -6px; }

  .tag-diamond {
    position: absolute; left: 566px; top: 86px; width: 277px; height: 277px;
    background: var(--purple); border-radius: 34px; transform: rotate(45deg);
  }
  .tagline {
    position: absolute; left: 539px; top: 166px; color: var(--white);
    font-weight: 700; font-size: 39px; line-height: 35px; letter-spacing: -1.5px;
  }

  .intro {
    position: absolute; left: 0; top: 428px; width: 927px; height: 96px;
    background: var(--slate); color: var(--white);
    padding: 9px 32px 0; font-size: 19.5px; line-height: 26px; font-weight: 400;
  }

  .tile { position: absolute; padding: 36px 0 0 30px; color: var(--ink); }
  .tile h2 { color: var(--white); font-weight: 700; font-size: 42px; line-height: 44px; letter-spacing: -2px; margin-bottom: 2px; }
  .tile li { list-style: none; font-size: 28px; line-height: 36px; letter-spacing: -1.6px; font-weight: 400; }
  .tile.narrow li { line-height: 30px; }

  .healthy { left: 0; top: 524px; width: 380px; height: 256px; background: var(--gold); }
  .fitness { left: 380px; top: 524px; width: 256px; height: 256px; background: var(--amber); padding-left: 35px; }
  .creativity { left: 636px; top: 524px; width: 291px; height: 256px; background: var(--orange); padding-left: 39px; }
  .mental { left: 0; top: 780px; width: 380px; height: 236px; background: var(--tangerine); padding-left: 29px; padding-top: 16px; box-shadow: inset 0 6px 6px -4px rgba(0,0,0,.25); }
  .financial { left: 380px; top: 780px; width: 547px; height: 236px; background: var(--flame); padding-left: 27px; padding-top: 16px; box-shadow: 0 4px 6px rgba(0,0,0,.2); }

  .badge {
    position: absolute; left: -6px; top: 1000px; width: 240px; height: 240px;
    background: var(--white); border-radius: 38px; transform: rotate(45deg);
  }
  .campaign-icons { position: absolute; left: 24px; top: 1018px; width: 162px; height: 122px; }
  .site { position: absolute; left: 141px; top: 1153px; font-size: 17px; color: var(--ink); }
</style>
</head>
<body>
<main class="poster">
  <header class="hero">
    <div class="headline perform">Perform</div>
    <div class="headline at">at</div>
    <div class="headline highest">Highest</div>
    <div class="headline capacity">Capacity</div>
    <div class="tag-diamond"></div>
    <p class="tagline">Be Your<br>Best Self</p>
  </header>

  <p class="intro">We are committed to providing programs that bring focus to your health and overall personal wellness to encourage a well balanced life</p>

  <section class="tile healthy">
    <h2>Healthy Living</h2>
    <ul><li>Health and wellness seminars</li><li>Nutrition: Fruit Delivery</li></ul>
  </section>
  <section class="tile fitness narrow">
    <h2>Fitness</h2>
    <ul><li>Step Challenge</li><li>Virtual 5k</li><li>Recess</li><li>Golf Lessons</li><li>Ping Pong Club</li></ul>
  </section>
  <section class="tile creativity narrow">
    <h2>Creativity</h2>
    <ul><li>Painting</li><li>Photography Club</li><li>Virtual Trivia</li></ul>
  </section>
  <section class="tile mental">
    <h2>Mental Health</h2>
    <ul><li>Massage Therapy</li><li>EAP Education</li></ul>
  </section>
  <section class="tile financial">
    <h2>Financial</h2>
    <ul><li>401(k)</li><li>Retirement education/financial<br>planning seminars</li><li>Global Insurance Program education</li></ul>
  </section>

  <div class="badge"></div>
  <svg class="campaign-icons" viewBox="0 0 162 122" role="img" aria-label="Cluster of four campaign icons in diamond tiles">
    <defs>
      <linearGradient id="iconTones" x1="0" y1="0" x2="1" y2="1">
        <stop offset="0" stop-color="#6c2c8c"/>
        <stop offset="0.5" stop-color="#f39a2b"/>
        <stop offset="1" stop-color="#1f9bb0"/>
      </linearGradient>
    </defs>
    <path d="M81 2 L160 61 L81 120 L2 61 Z" fill="url(#iconTones)"/>
  </svg>
  <div class="site">www.pelmaroq.com</div>
</main>
</body>
</html>
```